Webdesign für psychotherapeutische Praxis
Zielgruppe
Psychotherapeutische Praxis für erwachsene Patienten mit psychischen Erkrankungen.
Die Website soll eine solide, vertrauensvolle Information über das therapeutische Angebot bieten sowie alle Informationen zur Erstkontaktaufnahme erhalten.
Aufgabenstellung
Logo füge ich bei. Die Farben, das Design, die Schrift sollen dem Logo entsprechen (Grau, Violett-Pink Töne, moderne Schrift).

```html
<!DOCTYPE html>
<html lang="de">
<head>
<meta charset="utf-8">
<title>Psychotherapeutische Praxis – Therapieangebot</title>
<link href="https://fonts.googleapis.com/css2?family=Fira+Sans:wght@300;400;500&display=swap" rel="stylesheet">
<style>
:root{
  --violet:#6a5aa6;
  --violet-line:#a9a2c8;
  --text:#4a4a4a;
  --hero:#dcd0e3;
  --band:#6b6a6b;
  --footer:#4d4c4d;
  --white:#ffffff;
}
*{margin:0;padding:0;box-sizing:border-box}
html,body{width:727px;height:1200px;overflow:hidden}
body{position:relative;background:var(--white);font-family:"Fira Sans",sans-serif;font-weight:300;color:var(--text)}
.abs{position:absolute}
.site-header{left:0;top:0;width:727px;height:38px}
.brand{left:82px;top:7px;display:flex;align-items:center;gap:8px}
.brand-dot{width:18px;height:18px;border-radius:50%;background:#b98bd0}
.brand-text{font-size:5.2px;line-height:7px;color:#555;font-weight:400}
.nav{top:14px;font-size:8.6px;font-weight:400;color:#444}
.hero{left:0;top:38px;width:727px;height:106px;background:linear-gradient(90deg,var(--hero) 0%,var(--hero) 30%,#c9b9c2 65%,#b8a99e 100%)}
.title{color:var(--violet);font-weight:300}
.rule{height:1px;background:var(--violet-line)}
.quote{left:102px;top:242px;width:200px;font-size:12.6px;line-height:15.2px;font-weight:400;color:#444}
.quote-author{left:103px;top:307px;font-size:10.6px;color:var(--violet)}
.btn-outline{border:1px solid #444;font-size:9.3px;font-weight:400;color:#444;display:flex;align-items:center;justify-content:center}
.room-photo{left:338px;top:180px;width:276px;height:206px;background:linear-gradient(135deg,#d9d6d3 0%,#c4c1be 45%,#7d7b7a 75%,#565555 100%)}
.body-text{left:95px;width:520px;font-size:11.6px;line-height:14.4px}
.body-text strong{font-weight:400;color:#444}
.list{list-style:none}
.list li{padding-left:10px;text-indent:-10px}
.cta-band{left:0;top:950px;width:727px;height:85px;background:var(--band)}
.cta-text{left:156px;top:982px;font-size:17.5px;color:var(--white)}
.cta-btn{left:397px;top:979px;width:110px;height:28px;border:1.5px solid var(--white);color:var(--white);font-size:12px;font-weight:400;display:flex;align-items:center;justify-content:center}
.site-footer{left:0;top:1035px;width:727px;height:165px;background:var(--footer);color:var(--white)}
.foot-head{font-size:11px;font-weight:400;color:var(--white)}
.foot-rule{height:1px;background:#cfcfcf}
.foot-text{font-size:9px;line-height:11.2px;color:#eee}
.foot-icon{width:12px;height:14px}
</style>
</head>
<body>
<header class="site-header abs">
  <div class="brand abs">
    <span class="brand-dot"></span>
    <div class="brand-text">Psychotherapeutische Praxis<br>DIPL.-PSYCH. ANDREA HOLLMANN<br>Psychologische Psychotherapeutin (VT)</div>
  </div>
  <span class="nav abs" style="left:241px">Startseite</span>
  <span class="nav abs" style="left:318px">Therapieangebot</span>
  <span class="nav abs" style="left:431px">Therapieablauf</span>
  <span class="nav abs" style="left:532px">Über mich</span>
  <span class="nav abs" style="left:603px">Kontakt</span>
</header>

<div class="hero abs" role="img" aria-label="Blühende Baumzweige vor zartviolettem Himmel"></div>

<h1 class="title abs" style="left:102px;top:172px;font-size:21px">Therapieangebot</h1>
<div class="rule abs" style="left:102px;top:213px;width:148px"></div>
<p class="quote abs">„Es ist nicht genug zu wissen, man muss auch anwenden.<br>Es ist nicht genug zu wollen, man muss auch tun!“</p>
<span class="quote-author abs">J. W. Falkenberg</span>
<div class="btn-outline abs" style="left:102px;top:344px;width:79px;height:21px">Mehr erfahren</div>

<div class="room-photo abs" role="img" aria-label="Therapieraum mit zwei dunklen Sesseln, Beistelltischen und Wandbild"></div>

<h2 class="title abs" style="left:95px;top:424px;font-size:19.5px">Behandlung</h2>
<div class="rule abs" style="left:95px;top:462px;width:311px"></div>

<p class="body-text abs" style="top:479px;line-height:15.2px;font-size:12px">Das Therapieangebot richtet sich an Menschen mit behandlungsbedürftigen psychischen Erkrankungen ab dem Erwachsenenalter. Die therapeutischen Maßnahmen finden sowohl im Einzelsetting als auch in der Gruppe statt. Bitte fragen Sie nach Gruppenangeboten.</p>

<div class="body-text abs" style="top:548px">
  <strong style="font-size:12px">Behandlungsspektrum:</strong>
  <ul class="list">
    <li>-&nbsp; Affektive Störungen (Depressionen, Burnout)</li>
    <li>-&nbsp; Angststörungen (Panikstörungen, Phobien, Soziale Ängste, generalisierte Angststörung)</li>
    <li>-&nbsp; Borderline-Erkrankung</li>
    <li>-&nbsp; Essstörungen</li>
    <li>-&nbsp; Persönlichkeitsstörungen</li>
    <li>-&nbsp; Somatoforme Störungen</li>
    <li>-&nbsp; Traumafolgestörungen</li>
    <li>-&nbsp; Zwangsstörungen</li>
  </ul>
</div>

<div class="body-text abs" style="top:702px;width:460px">
  <strong style="font-size:12px">Behandlungsmethoden:</strong>
  <ul class="list">
    <li>-&nbsp; Kognitive Verhaltenstherapie</li>
    <li>-&nbsp; Traumatherapieverfahren (DBT der Posttraumatischen Belastungsstörung, Cognitive Processing Therapy)</li>
    <li>-&nbsp; Schematherapie</li>
  </ul>
</div>

<p class="body-text abs" style="top:804px;width:515px">Als Verhaltenstherapeutin fühle ich mich einem transparenten und aktivierenden Therapieansatz verpflichtet, der Hilfe zur Selbsthilfe ermöglicht.&nbsp; Unsere Gedanken und Gefühle haben einen entscheidenden Einfluss auf unser Verhalten. Mit Hilfe der kognitiven Verhaltenstherapie werden wir bisherige Denkweisen hinterfragen und ungünstige Verhaltensweisen identifizieren. Durch ihre aktive Mitarbeit, versuchen wir korrigierende Erfahrungen zu ermöglichen, die das Erleben der Selbstwirksamkeit entscheidend verbessern.</p>

<section class="cta-band abs"></section>
<span class="cta-text abs">Über den Ablauf der Therapie</span>
<div class="cta-btn abs">Mehr erfahren</div>

<footer class="site-footer abs">
  <span class="foot-head abs" style="left:150px;top:33px">Psychotherapeutische Praxis Hollmann</span>
  <div class="foot-rule abs" style="left:150px;top:50px;width:175px"></div>
  <svg class="foot-icon abs" style="left:151px;top:68px" viewBox="0 0 12 14"><path d="M6 1a4.5 4.5 0 0 0-4.5 4.5C1.5 9 6 13 6 13s4.5-4 4.5-7.5A4.5 4.5 0 0 0 6 1z" fill="none" stroke="#fff" stroke-width="1.2"/></svg>
  <p class="foot-text abs" style="left:168px;top:67px">Am Lindenhang 12<br>60431 Frankfurt/Main</p>
  <svg class="foot-icon abs" style="left:150px;top:100px" viewBox="0 0 12 14"><path d="M1 4c2-2.5 8-2.5 10 0l-1.5 1.5-2-1V3.5h-3v1l-2 1z" fill="#fff"/><g fill="#fff"><circle cx="4" cy="7.5" r=".8"/><circle cx="6" cy="7.5" r=".8"/><circle cx="8" cy="7.5" r=".8"/><circle cx="4" cy="9.8" r=".8"/><circle cx="6" cy="9.8" r=".8"/><circle cx="8" cy="9.8" r=".8"/><circle cx="6" cy="12" r=".8"/></g></svg>
  <p class="foot-text abs" style="left:168px;top:102px">0170 / 000 12 34</p>
  <svg class="foot-icon abs" style="left:150px;top:122px" viewBox="0 0 12 14"><path d="M11 2 1 7l4 1.5L6.5 12.5 11 2zM5 8.5 11 2" fill="none" stroke="#fff" stroke-width="1"/></svg>
  <p class="foot-text abs" style="left:167px;top:124px">hollmann-therapie@postfach-mail.de</p>

  <span class="foot-head abs" style="left:386px;top:33px">Hinweis</span>
  <div class="foot-rule abs" style="left:386px;top:50px;width:72px"></div>
  <p class="foot-text abs" style="left:386px;top:57px">Aufgrund der&nbsp; Coronavirus /SARS-CoV-2- Krise<br>biete ich zertifizierte Videosprechstunden an!</p>
  <span class="foot-head abs" style="left:386px;top:88px">Telefonische Erreichbarkeit</span>
  <div class="foot-rule abs" style="left:386px;top:105px;width:130px"></div>
  <p class="foot-text abs" style="left:386px;top:112px">Montags, dienstags, Mittwochs &amp; Donnerstags<br>von 13:00 bis 13:30 Uhr</p>
</footer>
</body>
</html>
```